Health care center needs brochure design

We need a set of brochure designs for the 4 sections of our clinic, color coded based on the brand guidelines and with introduced icons to every section. The three sections include Biological Medicine (main medication tool is the IV tool), The golden tide program (main medication tool are the detox tools) , the Aesthetics section ( main medication tool is the syringe) and the lab (main tool is the microscope). You can find out more about our sections in the website www.drvelnor.com. The use of elements of the brand itself such as the lotus is also applicable.

Industry/Entity Type

Health Care

Requirements
Must have
• use of brand identity colors and features
• reflective medical icons
• color coding for each of the 4 sections based on the brand colors
Should not have
• pictures overused by other health care providers

```html
<!DOCTYPE html>
<html lang="en">
<head>
<meta charset="utf-8">
<title>Dr Velnor Integrated Care Center – Section Brochures</title>
<link href="https://fonts.googleapis.com/css2?family=Montserrat:wght@300;400;500;600&display=swap" rel="stylesheet">
<style>
:root{
  --page:#f3f2ef;
  --paper:#ffffff;
  --blue:#b6d3ef;
  --blue-ink:#7fb2dc;
  --green:#71c6ac;
  --green-ink:#46b093;
  --pink:#e3b7af;
  --pink-ink:#df9684;
  --pink-text:#9c6f66;
  --peach:#f8b58d;
  --peach-ink:#f08c5f;
  --grey:#6d6d6d;
  --dark:#333;
}
*{margin:0;padding:0;box-sizing:border-box}
html,body{width:1200px;height:2198px;overflow:hidden;background:var(--page);font-family:"Montserrat",sans-serif;color:var(--grey)}
.spread{position:absolute;left:51px;width:1096px;height:388px;display:flex;box-shadow:0 3px 10px rgba(0,0,0,.12)}
.panel{position:relative;width:548px;height:100%;background:var(--paper)}
.panel.left{background:linear-gradient(90deg,#fff 80%,#f1f1f1)}
.brand{display:flex;align-items:center;gap:8px;font-weight:500;color:var(--green-ink)}
.brand .dot{border-radius:50%;background:var(--peach);flex:none}
.mini-brand{position:absolute;left:28px;top:30px;font-size:9px;line-height:1.2}
.mini-brand .dot{width:22px;height:22px}
.divider{position:absolute;left:425px;top:30px;width:1px;height:100px;background:#ddd}
.icon-slot{position:absolute;left:445px;top:30px;width:70px;height:100px;border-radius:6px}
.section-title{position:absolute;left:28px;font-size:20px;font-weight:500;letter-spacing:.5px}
.body-copy{position:absolute;left:28px;width:483px;font-size:13px;line-height:14.3px;font-weight:300}
.list-head{font-size:15px;font-weight:500;color:#fff;letter-spacing:.4px;margin-bottom:10px;padding-bottom:8px;position:relative}
.list-head::after{content:"";position:absolute;left:0;bottom:0;width:26px;height:1px;background:#fff}
.list{list-style:none;font-size:13.5px;line-height:24.5px;font-weight:300;color:#fff}
.corner-brand{position:absolute;right:26px;bottom:26px;font-size:7px;color:#fff;line-height:1.2}
.corner-brand .dot{width:26px;height:26px;background:#fff}
</style>
</head>
<body>

<!-- Cover -->
<section class="spread" style="top:40px">
  <div class="panel left">
    <div style="position:absolute;left:28px;top:253px;font-size:14px;line-height:16px">
      <p style="font-weight:500;color:var(--green-ink)">Dr Velnor Integrated Care Center</p>
      <p style="color:var(--green);font-weight:300">POBox 40210</p>
      <p style="color:var(--green);font-weight:300">Harbor District, Cedar Quarter</p>
      <p style="color:var(--green);font-weight:300">United Arab Emirates</p>
      <p style="font-size:20px;font-weight:500;color:var(--dark);margin-top:6px;line-height:22px">02-555 0147</p>
      <p style="color:var(--dark);font-weight:300">info@drvelnor.com</p>
    </div>
    <div style="position:absolute;left:460px;top:336px;width:22px;height:22px;background:#3b5b9f;border-radius:3px"></div>
    <div style="position:absolute;left:494px;top:336px;width:22px;height:22px;background:#e4336d;border-radius:3px"></div>
  </div>
  <div class="panel">
    <div class="brand" style="position:absolute;left:218px;top:136px;font-size:15px;line-height:1.3;gap:14px">
      <span class="dot" style="width:108px;height:108px"></span>
      <span>DR VELNOR<br>INTEGRATED<br>CARE CENTER</span>
    </div>
  </div>
</section>

<!-- Program intro -->
<section class="spread" style="top:463px">
  <div class="panel left">
    <h2 class="section-title" style="top:24px;font-size:17px;color:var(--blue-ink)">THE VITACHECK PROGRAM</h2>
    <div class="body-copy" style="top:56px">
      <p>VITACHECK is a program for early diagnosis of pathophysiological imbalances associated with lifestyle and environmental diseases. Prompt diagnosis of early-stage metabolic imbalances, before they progress into overt disease, will motivate you to take appropriate steps; such steps can reverse disease progression and restore optimal health.</p>
      <p style="margin-top:14px">By limiting calorie intake, following a balanced diet, and engaging in physical activity, it is often possible to restore your health and well-being and to maintain an age appropriate state of health. Furthermore, your genetic makeup, which differs from person to person, has a long-term impact on your health. However, in an optimized environment (physical and social activity, diet, etc.), gene expression can be modified, thereby lowering the risk of disease. This approach also decreases the risk of a large number of age-linked degenerative diseases.</p>
      <p style="margin-top:14px">When your patients gain awareness of their state of health, with support provided by objective laboratory analyses and personalized advice, they will also gain the motivation needed to fulfill their responsibilities for keeping healthy.</p>
    </div>
  </div>
  <div class="panel" style="background:var(--blue)">
    <div style="position:absolute;left:224px;top:108px;width:100px;height:100px;border-radius:50%;background:#fff"></div>
    <p style="position:absolute;left:0;width:100%;top:238px;text-align:center;color:#fff;font-size:20px;font-weight:500">Dr Velnor</p>
    <p style="position:absolute;left:0;width:100%;top:266px;text-align:center;color:#fff;font-size:15px;font-weight:300">Integrated Care Center</p>
  </div>
</section>

<!-- Biological medicine -->
<section class="spread" style="top:883px">
  <div class="panel left">
    <div class="brand mini-brand"><span class="dot"></span><span>DR VELNOR<br>INTEGRATED<br>CARE CENTER</span></div>
    <span class="divider"></span>
    <div class="icon-slot" role="img" aria-label="Line icon of an IV drip bag" style="background:#e3f4ee"></div>
    <h2 class="section-title" style="top:184px;color:var(--green-ink)">BIOLOGICAL MEDICINE</h2>
    <p class="body-copy" style="top:220px">The Center provides a combination of therapies and diagnostics relevent to each individuals case. It is recomended that the patient passes through consultation prior to going through any type of treatment as the practitioner studies thoroughly specific elements of the persons condition and directs them towards the best therapy course.</p>
  </div>
  <div class="panel" style="background:var(--green)">
    <div style="position:absolute;left:40px;top:26px">
      <h3 class="list-head">WE SPECIALIZE IN</h3>
      <ul class="list">
        <li>General Medical Consultation</li><li>Healthy Lifestyle consultation</li><li>Magnetic Field Therapy</li>
        <li>Detoxification using Pressotherapy</li><li>Orthomolecular concepts</li><li>Nutritional consultations</li>
        <li>Kinesiology, body mind therapy</li><li>IV's immune syst. stimulation (Vit. C)</li><li>Chelation IV</li>
        <li>Neural therapy, injections</li><li>Lymphatic Drainage</li><li>Manual massages</li>
      </ul>
    </div>
    <div style="position:absolute;left:341px;top:26px">
      <h3 class="list-head" style="line-height:17px">OUR DIAGNOSTICS<br>INCLUDE</h3>
      <ul class="list" style="line-height:23.5px">
        <li>Vitacheck up</li><li>Darkfield microscopy</li><li>Mineral scan</li><li>Heart rate variability</li>
        <li>Lab: heavy metal lab</li><li>Lab: hormones</li><li>Lab: stool test</li><li>Lab: fatty acid profiles</li><li>Lab: food intolerance</li>
      </ul>
    </div>
    <div class="brand corner-brand" style="color:#fff"><span class="dot"></span><span>DR VELNOR<br>INTEGRATED<br>CARE CENTER</span></div>
  </div>
</section>

<!-- Golden tide program -->
<section class="spread" style="top:1317px">
  <div class="panel left">
    <div class="brand mini-brand"><span class="dot"></span><span>DR VELNOR<br>INTEGRATED<br>CARE CENTER</span></div>
    <span class="divider"></span>
    <div class="icon-slot" role="img" aria-label="Line illustration of detox herbs" style="background:#f6e3df"></div>
    <h2 class="section-title" style="top:158px;color:var(--pink-ink)">GOLDEN TIDE PROGRAM</h2>
    <p class="body-copy" style="top:194px">Maintaining a healthy lifestyle is a personal goal for everyone, whether you have had a treatment for something or simply wish to ensure you are always at a healthy natural state, the center will help facilitate that. Maintaining health is the way to control your body weight, have an amazing skin, and avoid risks of getting diseases. Releasing toxins and negative energy revives the body's internal health and naturally reflects on its organic system. A set of detox and nutritional programs in addition to tapping and sound therapies are provided by the center for your satisfaction and health from within.</p>
  </div>
  <div class="panel" style="background:var(--pink)">
    <div style="position:absolute;left:172px;top:32px">
      <h3 class="list-head" style="color:var(--pink-text)">CONDITIONS WE TREAT</h3>
      <ul class="list" style="color:var(--pink-text)">
        <li>Weight loss/gain</li><li>Digestive Conditions</li><li>Skin Conditions</li><li>Chronic Headaches and Migraines</li>
        <li>Fatigue and Insomnia</li><li>Allergies</li><li>Depression</li><li>Joints Conditions</li>
        <li>Muscle Conditions</li><li>Neural Conditions</li><li>Hyperacidity</li>
      </ul>
    </div>
    <div class="brand corner-brand"><span class="dot"></span><span>DR VELNOR<br>INTEGRATED<br>CARE CENTER</span></div>
  </div>
</section>

<!-- Aesthetics -->
<section class="spread" style="top:1742px">
  <div class="panel left">
    <div class="brand mini-brand"><span class="dot"></span><span>DR VELNOR<br>INTEGRATED<br>CARE CENTER</span></div>
    <span class="divider"></span>
    <div class="icon-slot" role="img" aria-label="Line icon of a syringe" style="background:#fde9dc"></div>
    <h2 class="section-title" style="top:198px;color:var(--peach-ink)">AESTHETICS</h2>
    <p class="body-copy" style="top:232px">We like to see you glowing inside out, so to compliment our holistic services we provide the latest Aesthetic skin care technologies and treatments. The center provides unique blends of vitamins and minerals for skin rejuvenation. Beauty comes from within, adding a bit care to boost your spirit and look glamorous is a plus we thrive to provide.</p>
  </div>
  <div class="panel" style="background:var(--peach)">
    <div style="position:absolute;left:28px;top:26px">
      <h3 class="list-head">OUR TREATMENTS INCLUDE</h3>
      <ul class="list" style="font-size:13px;line-height:21px">
        <li style="font-weight:500">Face Treatment</li><li>Crystal Peeling</li><li>Face Lifting - PRP</li><li>Anti-Wrinkle and Lip treatment</li>
        <li>Puffy Eye Treatment</li><li>Acne Treatment alternatives</li><li>Mesotherapy</li><li>Velora Skin Solutions Micro-needling</li>
        <li>Stem Cell Serum  Micro-needling</li><li>LED Light therapy face mask</li><li>Oxygen/Hyaluronic Acid Infusion</li>
        <li>Hydra-Dermabrasion</li><li>Micro-Dermabrasion</li>
      </ul>
    </div>
    <div style="position:absolute;left:299px;top:26px;width:200px">
      <ul class="list" style="font-size:13px;line-height:17px">
        <li style="font-weight:500;margin-bottom:7px">Body Treatment</li>
        <li>Slimming and Body Firming</li><li>Fat Freeze (Cryolipolysis)</li>
        <li style="font-weight:500;margin:4px 0 7px">Hair Treatments</li>
        <li>Hair restoration treatment with Velora Skin Solutions</li>
        <li style="margin-top:6px">Hair reduction treatment with Laser Technology</li>
        <li style="margin-top:6px">Eye Lash Enhancer</li>
      </ul>
      <h3 class="list-head" style="margin-top:22px;line-height:17px">OUR DIAGNOSIS<br>INCLUDE</h3>
      <ul class="list" style="font-size:13px;line-height:18px"><li>Body Analyzer</li><li>Facial Analysis</li></ul>
    </div>
    <div role="img" aria-label="Line icon of a microscope" style="position:absolute;left:455px;top:262px;width:64px;height:84px;border-radius:6px;background:#fbcdb0"></div>
  </div>
</section>

</body>
</html>
```